Web Design for photo printing service

Hi
I am looking for a new web design theme for our almost ready website http://glerhorn.tqzs.net, it will soon be launched under the name: www.zuba-web.is. (ZUBA means: Zest Under Bright Arches)

This is a website focused on printing photo products like: photo books, Greeting cards, posters, etc.

The whole theme should be playful, fun, creative. The marketing will be is that Life is fun, keep your memories. remember the good time etc.

So what I am looking for is a simple, yet colorful theme, easy to use.

We will be running max 4- 6 product groups, all extra info should be on the button,
expect shopping chart and sign in should be on top.

Extra feature:
Once a year during christmas, the web will turn on christmas outfit, it transforms
to Christmas looking Web. So a X-mas version would be fun to see !

Young people 20-35, young families.

Printing

• Fun looking colorful design, simple to use.
• Dark heavy look

```html
<!DOCTYPE html>
<html lang="en">
<head>
<meta charset="utf-8">
<title>ZUBA – Photo Books</title>
<link href="https://fonts.googleapis.com/css2?family=Ubuntu:wght@400;500;700&family=Roboto:wght@300;400&display=swap" rel="stylesheet">
<style>
:root{
  --nav:#2e2e2e;
  --nav-line:#444;
  --pink:#e4007c;
  --teal:#1b9ec0;
  --purple:#a2258f;
  --page:#e2e2e2;
  --panel:#ffffff;
  --card-line:#c9c9c9;
  --text:#333;
  --footer:#2b2b2b;
  --footer-text:#8d8d8d;
  --field:#3a3a3a;
  --orange:#f47c45;
}
*{box-sizing:border-box;margin:0;padding:0}
html,body{width:811px;height:1200px;overflow:hidden}
body{position:relative;background:var(--page);font-family:"Roboto",Arial,sans-serif;color:var(--text)}
.abs{position:absolute}

/* top navigation */
.topnav{left:0;top:0;width:811px;height:44px;background:var(--nav);display:flex}
.topnav a{color:#fff;text-decoration:none;font:500 12px "Ubuntu",sans-serif;display:flex;align-items:center;justify-content:center;border-right:1px solid var(--nav-line)}
.cart{flex:1;background:#3a3a3a;color:#fff;font:10px "Roboto",sans-serif;display:flex;align-items:center;padding-left:16px;gap:8px}
.cart small{font-size:8px;color:#bbb}
.cart small u{color:var(--pink)}
.cart svg{flex:none}

/* header */
.header{left:0;top:44px;width:811px;height:164px;background:linear-gradient(180deg,#d9d9d9 0%,#f6f6f6 45%,#eeeeee 100%)}
.hero-photo{right:0;top:0;width:210px;height:164px;background:radial-gradient(circle at 75% 40%,#5a5a5a 0%,#9a9a9a 40%,rgba(230,230,230,0) 75%)}
.account{right:0;top:1px;width:128px;height:18px;background:#efefef;font:9px "Roboto",sans-serif;color:#222;display:flex;align-items:center;justify-content:center}
.brand{left:48px;top:42px;display:flex;align-items:center;gap:14px}
.brand-mark{width:50px;height:50px;border-radius:50%;background:var(--pink)}
.brand-name{font:700 74px/1 "Ubuntu",sans-serif;color:var(--teal);letter-spacing:2px}
.tagline{left:120px;top:126px;font:500 11px "Ubuntu",sans-serif;color:#333}
.divider{left:0;top:208px;width:811px;height:6px;background:#fff}

/* sidebar */
.side-item{left:48px;width:171px;height:116px}
.side-item h3{height:22px;background:var(--nav);color:#fff;font:500 12px/22px "Ubuntu",sans-serif;padding-left:7px}
.side-item .thumb{height:94px;position:relative}
.side-item a{position:absolute;right:0;bottom:0;background:#fff;color:var(--pink);font-size:9px;padding:6px 12px 5px 13px}

/* content */
.panel{left:231px;top:234px;width:532px;height:666px;background:var(--panel)}
.panel h1{position:absolute;left:18px;top:12px;font:700 16px "Ubuntu",sans-serif;color:var(--pink)}
.intro{position:absolute;left:19px;top:41px;width:500px;font-size:9px;line-height:12.5px;color:#333}
.intro p+p{margin-top:12px}
.card{width:155px;height:245px;border:1px solid var(--card-line);background:#fff}
.card .pic{width:62px;height:56px;margin:8px auto 0;border-radius:3px}
.card h2{margin-top:7px;border-top:1px solid #ddd;border-bottom:1px solid #ddd;height:18px;font:500 10.5px/18px "Ubuntu",sans-serif;color:#555;padding-left:9px;letter-spacing:.2px}
.card p{padding:8px 9px 0;font-size:8.6px;line-height:12.5px;color:#444}
.card .actions{position:absolute;left:10px;bottom:8px;display:flex;gap:4px}
.btn{font-size:8.6px;color:#fff;text-decoration:underline;height:19px;line-height:19px;padding:0 6px}
.btn.know{background:var(--teal);width:56px}
.btn.create{background:var(--purple);width:57px;text-align:center}

/* footer */
.band{left:0;top:912px;width:811px;height:7px;background:#fff}
.footer{left:0;top:919px;width:811px;height:281px;background:var(--footer);color:var(--footer-text)}
.footer h4{position:absolute;top:32px;font:500 13px "Ubuntu",sans-serif;color:#fff}
.quote-photo{left:65px;top:58px;width:57px;height:52px;background:linear-gradient(160deg,#6d6d6d,#2a2a2a)}
.quote-name{left:129px;top:60px;font:500 13px "Ubuntu",sans-serif;color:#9a9a9a}
.quote-role{left:129px;top:80px;font:8px "Roboto",sans-serif;color:#aaa}
.quote-text{left:67px;top:124px;width:150px;font-size:9px;line-height:12.5px;color:#8a8a8a}
.follow{left:288px;display:flex;align-items:center;gap:12px;font-size:9.5px;color:#999}
.follow span{width:24px;height:24px;border-radius:50%}
.field-label{left:526px;font-size:9px;color:#999}
.field{left:571px;width:177px;background:var(--field);border-radius:2px}
.submit{left:694px;top:170px;width:52px;height:24px;background:#fff;border-radius:3px;color:#333;font-size:9.5px;display:flex;align-items:center;justify-content:center}
.rule{left:63px;top:222px;width:697px;height:1px;background:#4a4a4a}
.to-top{left:64px;top:234px;width:34px;height:34px;border-radius:50%;background:var(--orange)}
.links{right:78px;top:245px;font-size:9px;color:#ddd;text-align:right;line-height:12px}
.links small{display:block;color:#555;font-size:9px}
</style>
</head>
<body>

<nav class="topnav abs">
  <a style="width:93px">Photo Books</a>
  <a style="width:94px">Calendars</a>
  <a style="width:95px">Posters</a>
  <a style="width:95px">Map</a>
  <a style="width:130px">Printed Photographs</a>
  <a style="width:94px">Our Prices</a>
  <div class="cart">
    <svg width="18" height="14" viewBox="0 0 18 14"><path d="M1 4h16l-2 9H3z" fill="none" stroke="#bbb" stroke-width="1.4"/><path d="M5 4l3-3M13 4l-3-3" stroke="#bbb" stroke-width="1.4"/></svg>
    <span>Shopping cart: <small>Now in your cart <u>0 items</u></small></span>
  </div>
</nav>

<header class="header abs">
  <div class="hero-photo abs" role="img" aria-label="Photographer holding a video camera on his shoulder, in black and white"></div>
  <div class="account abs">Create an account | Login</div>
  <div class="brand abs">
    <div class="brand-name">ZUBA</div>
    <div class="brand-mark"></div>
  </div>
  <div class="tagline abs">Zest Under Bright Arches</div>
</header>
<div class="divider abs"></div>

<aside>
  <div class="side-item abs" style="top:232px">
    <h3>Photo Books</h3>
    <div class="thumb" role="img" aria-label="Open scrapbook photo album with a family picture" style="background:linear-gradient(135deg,#c8645a,#e6b6a8 50%,#b14a6a)"><a>Read more</a></div>
  </div>
  <div class="side-item abs" style="top:357px">
    <h3>Calendars</h3>
    <div class="thumb" role="img" aria-label="Desk calendars stacked on a table" style="background:linear-gradient(135deg,#cfd3d6,#eef0f1 60%,#b8bdc0)"><a>Read more</a></div>
  </div>
  <div class="side-item abs" style="top:480px">
    <h3>Posters</h3>
    <div class="thumb" role="img" aria-label="Typographic poster with yellow lettering on a dark background" style="background:linear-gradient(135deg,#3a3a32,#5d5a3c 60%,#2e2d28)"><a>Read more</a></div>
  </div>
  <div class="side-item abs" style="top:603px">
    <h3>Map</h3>
    <div class="thumb" role="img" aria-label="Christmas greeting cards laid on a table" style="background:linear-gradient(135deg,#f1ece4,#e7c9c0 55%,#cfe3e6)"><a>Read more</a></div>
  </div>
  <div class="side-item abs" style="top:727px">
    <h3>Printed Photographs</h3>
    <div class="thumb" role="img" aria-label="Printed photographs spread over a wooden desk" style="background:linear-gradient(135deg,#5a4a3e,#a89484 55%,#3d332c)"><a>Read more</a></div>
  </div>
</aside>

<main class="panel abs">
  <h1>PHOTO BOOKS</h1>
  <div class="intro">
    <p>Your own photographs? Why? We know that your images deserve to be preserved. Even probably the best pictures in the world - so practically. You choose the front page, page masses, the size of the images and can add frames and all kinds. The book will then be printed, bound and shipped to your home. That's it been.</p>
    <p>You can have a book with pictures of the child, one for the dog. So you can do all kinds of books. For example, picture book with a single socks. They deserve not one of them take a picture? They are of course prepared to lose the other half. Or just jólabók, fermingarbók, giftingarbók or sumarbók. Let imaginations loose! ZUBA!</p>
  </div>
</main>

<section class="cards">
  <article class="card abs" style="left:250px;top:381px">
    <div class="pic" role="img" aria-label="Photo book with an autumn leaf cover" style="background:linear-gradient(135deg,#8a3b12,#e0a040)"></div>
    <h2>PHOTOGRAPHS 15X10 CM</h2>
    <p>Photographs in the photo size. The size of the book is very good on the shelf. Since she is also at photo book would be ideal to put in pictures of her short friends, small objects, pets (such as kittens and puppies) or children. But it may also post pictures of a big thing ...</p>
    <div class="actions"><span class="btn know">Know more</span><span class="btn create">Create</span></div>
  </article>
  <article class="card abs" style="left:420px;top:381px">
    <div class="pic" role="img" aria-label="Photo book with a swimmer in blue water" style="background:linear-gradient(135deg,#2e8ca0,#8cc7cf)"></div>
    <h2>PHOTOGRAPHS 21X15 CM</h2>
    <p>Photographs in the photo size. The size of the book is very good on the shelf. Since she is also at photo book would be ideal to put in pictures of her short friends, small objects, pets (such as kittens and puppies) or children. But it may also post pictures of a big thing ...</p>
    <div class="actions"><span class="btn know">Know more</span><span class="btn create">Create</span></div>
  </article>
  <article class="card abs" style="left:589px;top:381px">
    <div class="pic" role="img" aria-label="Square photo book with a toy figure on a dark cover" style="width:40px;background:linear-gradient(135deg,#2a1a1a,#a02a2a)"></div>
    <h2>PHOTOGRAPHS 21X21 CM</h2>
    <p>Photographs in the photo size. The size of the book is very good on the shelf. Since she is also at photo book would be ideal to put in pictures of her short friends, small objects, pets (such as kittens and puppies) or children. But it may also post pictures of a big thing ...</p>
    <div class="actions"><span class="btn know">Know more</span><span class="btn create">Create</span></div>
  </article>
  <article class="card abs" style="left:250px;top:638px">
    <div class="pic" role="img" aria-label="Stack of landscape prints with a tree at sunset" style="width:50px;background:linear-gradient(135deg,#d98a20,#6a7a20)"></div>
    <h2>PHOTOGRAPHS 21X30 CM</h2>
    <p>Photographs in the photo size. The size of the book is very good on the shelf. Since she is also at photo book would be ideal to put in pictures of her short friends, small objects, pets (such as kittens and puppies) or children. But it may also post pictures of a big thing ...</p>
    <div class="actions"><span class="btn know">Know more</span><span class="btn create">Create</span></div>
  </article>
  <article class="card abs" style="left:420px;top:638px">
    <div class="pic" role="img" aria-label="Stack of prints showing sailing boats" style="width:72px;background:linear-gradient(135deg,#5a7a9a,#c8d6e2)"></div>
    <h2>PHOTOGRAPHS 30X21 CM</h2>
    <p>Photographs in the photo size. The size of the book is very good on the shelf. Since she is also at photo book would be ideal to put in pictures of her short friends, small objects, pets (such as kittens and puppies) or children. But it may also post pictures of a big thing ...</p>
    <div class="actions"><span class="btn know">Know more</span><span class="btn create">Create</span></div>
  </article>
</section>

<div class="band abs"></div>
<footer class="footer abs">
  <h4 style="left:63px">Testimonial</h4>
  <div class="quote-photo abs" role="img" aria-label="Portrait of the customer giving the testimonial"></div>
  <div class="quote-name abs">DAN MERROW</div>
  <div class="quote-role abs">PHOTO STUDIO</div>
  <p class="quote-text abs">Morbi tempor quam vel massa adipiscing ute cursus micong. Aenean nonummy hendrerit mau phasellu porta. Fusce suscipit varius mi sed. Cum sociis natoque penatibus et magnis dis parturient...</p>

  <h4 style="left:292px">Follow Me</h4>
  <div class="follow abs" style="top:62px"><span style="background:#d8262c"></span>Watch me on Clipora</div>
  <div class="follow abs" style="top:92px"><span style="background:#f0812b"></span>RSS Feed</div>
  <div class="follow abs" style="top:123px"><span style="background:#3fb0d8"></span>Follow me on Tweetlane</div>
  <div class="follow abs" style="top:152px"><span style="background:#3b5a98"></span>Be a fan Pagebook</div>

  <h4 style="left:532px">Contact ZUBA</h4>
  <div class="field-label abs" style="top:75px">Name*</div>
  <div class="field abs" style="top:60px;height:24px"></div>
  <div class="field-label abs" style="top:105px">E-mail*</div>
  <div class="field abs" style="top:91px;height:24px"></div>
  <div class="field-label abs" style="top:136px">Text*</div>
  <div class="field abs" style="top:121px;height:40px"></div>
  <div class="submit abs">Submit</div>

  <div class="rule abs"></div>
  <div class="to-top abs">
    <svg width="34" height="34" viewBox="0 0 34 34"><path d="M17 8l-9 9h6v9h6v-9h6z" fill="#fff"/></svg>
  </div>
  <div class="links abs">Home | The small print | What do you want to know | Rates | About Us | Contact<small>ZUBA © 2013 | Privacy Policy</small></div>
</footer>

</body>
</html>
```